Maplebrook Self Storage - Business Sign

The sign we are needing designed is our main road sign for our self-storage business. The dimensions of the sign are 57 inches tall x 96 inches wide. We require that our attached logo be on the sign as well as our phone number: 478-216-7745 and website www.MaplebrookStorage.net. Optional information that can be added but not required is our address: 418 Delmont Ridge Pkwy, Centerville, GA 31044.

Industry/Entity Type

Self Storage

Font styles to use
Sans Serif

```html
<!DOCTYPE html>
<html lang="en">
<head>
<meta charset="utf-8">
<title>Maplebrook Self Storage – Road Sign Options</title>
<link rel="stylesheet" href="https://fonts.googleapis.com/css2?family=Montserrat:wght@500;600;700&display=swap">
<style>
  :root {
    --backdrop: #cbe0f4;
    --card-white: #ffffff;
    --card-edge: #2b2b2b;
    --brand-blue: #1f5dab;
    --charcoal: #464646;
    --rule-grey: #9a9a9a;
    --wordmark: #444444;
    --label-tint: #e6f0fa;
  }
  * { box-sizing: border-box; margin: 0; padding: 0; }
  html, body {
    width: 1200px; height: 1200px; overflow: hidden;
    background: var(--backdrop);
    font-family: "Montserrat", sans-serif;
  }
  .sheet { position: relative; width: 1200px; height: 1200px; }

  .sign {
    position: absolute; left: 180px; width: 840px; height: 498px;
    background: var(--card-white);
    border: 1px solid var(--card-edge);
    overflow: hidden;
  }
  .sign--opt1 { top: 80px; }
  .sign--opt2 { top: 630px; }

  .wordmark {
    position: absolute; left: 0; right: 0; top: 92px;
    text-align: center; color: var(--wordmark); font-weight: 600;
    line-height: 1;
  }
  .wordmark__name { display: block; font-size: 84px; letter-spacing: 1px; }
  .wordmark__sub { display: block; font-size: 44px; letter-spacing: 11px; margin-top: 22px; padding-left: 11px; }

  .divider { position: absolute; left: 0; right: 0; height: 6px; }
  .sign--opt1 .divider { top: 334px; background: var(--rule-grey); }
  .sign--opt2 .divider { top: 332px; background: var(--brand-blue); }

  .contact-band {
    position: absolute; left: 0; right: 0; bottom: 0; top: 345px;
  }
  .sign--opt1 .contact-band { background: var(--brand-blue); }
  .sign--opt2 .contact-band { background: var(--charcoal); top: 344px; }

  .phone {
    position: absolute; left: 0; right: 0; top: 14px;
    text-align: center; color: #fff; font-weight: 700;
    font-size: 62px; letter-spacing: 1px; line-height: 1;
  }
  .web {
    position: absolute; left: 188px; right: 188px; top: 94px; height: 28px;
    display: flex; align-items: center; justify-content: center;
    color: #fff; font-weight: 600; font-size: 19px; letter-spacing: 0.5px;
  }
  .sign--opt1 .web {
    background: linear-gradient(90deg, rgba(31,93,171,0), rgba(120,150,200,0.55) 25%, rgba(120,150,200,0.55) 75%, rgba(31,93,171,0));
  }
  .sign--opt2 .web {
    background: linear-gradient(90deg, rgba(70,70,70,0), rgba(31,93,171,0.8) 25%, rgba(31,93,171,0.8) 75%, rgba(70,70,70,0));
  }

  .option-label {
    position: absolute; left: 1040px;
    color: var(--label-tint); font-weight: 500; font-size: 30px;
  }
  .option-label--1 { top: 538px; }
  .option-label--2 { top: 1092px; }
</style>
</head>
<body>
<main class="sheet">
  <section class="sign sign--opt1" aria-label="Sign option 1">
    <div class="wordmark">
      <span class="wordmark__name">Maplebrook</span>
      <span class="wordmark__sub">SELF STORAGE</span>
    </div>
    <div class="divider"></div>
    <div class="contact-band">
      <p class="phone">478-216-7745</p>
      <p class="web">www.MaplebrookStorage.net</p>
    </div>
  </section>
  <span class="option-label option-label--1">Opt1</span>

  <section class="sign sign--opt2" aria-label="Sign option 2">
    <div class="wordmark">
      <span class="wordmark__name">Maplebrook</span>
      <span class="wordmark__sub">SELF STORAGE</span>
    </div>
    <div class="divider"></div>
    <div class="contact-band">
      <p class="phone">478-216-7745</p>
      <p class="web">www.MaplebrookStorage.net</p>
    </div>
  </section>
  <span class="option-label option-label--2">Opt2</span>
</main>
</body>
</html>
```